First Aid Training business needs business card design

We would like a double sided business card designed for a first aid training business - Brindlewood First Aid. We provide first aid training and , WHS (work, health and safety) training.

The attached word document contains the key information we would like on each side of the business card.

Final design needs to be delivered in print ready format, along with the original file.

```html
<!DOCTYPE html>
<html lang="en">
<head>
<meta charset="utf-8">
<title>Brindlewood First Aid – Business Card</title>
<link rel="stylesheet" href="https://fonts.googleapis.com/css2?family=Montserrat:wght@500;600;700&display=swap">
<style>
  :root {
    --bg: #e4e4e4;
    --card: #ffffff;
    --ink: #111111;
    --red: #ee0000;
    --grey: #8a8a8a;
  }
  * { box-sizing: border-box; margin: 0; padding: 0; }
  html, body { width: 967px; height: 1200px; overflow: hidden; }
  body {
    background: var(--bg);
    font-family: "Montserrat", sans-serif;
    color: var(--ink);
    position: relative;
  }
  .card {
    position: absolute;
    top: 488px;
    width: 392px;
    height: 223px;
    background: var(--card);
    border-radius: 22px;
    overflow: hidden;
    box-shadow: 2px 4px 6px rgba(0,0,0,0.35);
  }

  /* Front */
  .card--front { left: 65px; }
  .front-panel {
    position: absolute; left: 0; top: 0; bottom: 0; width: 127px;
    background: var(--ink);
    color: #fff;
    display: flex; flex-direction: column; align-items: center;
  }
  .brand-mark {
    margin-top: 24px;
    width: 78px; height: 78px; border-radius: 50%;
    background: var(--grey);
  }
  .front-panel__services {
    margin-top: 34px;
    font-size: 11.5px; font-weight: 700; line-height: 1.3;
    text-align: center;
  }
  .front-body { position: absolute; left: 140px; right: 14px; top: 30px; }
  .brand-name {
    font-size: 19px; font-weight: 700; line-height: 1.05;
    text-transform: uppercase; letter-spacing: 0.3px;
  }
  .tagline {
    display: inline-block; margin-top: 20px;
    background: var(--red); color: #fff;
    font-size: 8.6px; font-weight: 700; letter-spacing: 0.6px;
    padding: 4px 5px;
  }
  .benefits { list-style: none; margin-top: 9px; }
  .benefits li {
    display: flex; align-items: center; gap: 11px;
    font-size: 9px; font-weight: 600; letter-spacing: 0.6px;
    height: 25px;
  }
  .bullet {
    width: 11px; height: 11px; background: var(--red);
    box-shadow: 3px 3px 0 var(--ink); flex: none;
  }

  /* Back */
  .card--back { left: 511px; }
  .back-strip {
    position: absolute; left: 0; top: 0; bottom: 0; width: 33px;
    background: linear-gradient(var(--red) 0 75%, var(--ink) 75% 100%);
  }
  .back-tab { position: absolute; left: 91px; width: 47px; height: 18px; }
  .back-tab--top { top: 0; background: var(--red); }
  .back-tab--bottom { bottom: 0; background: var(--ink); }
  .back-brand {
    position: absolute; left: 45px; width: 140px; top: 60px;
    display: flex; flex-direction: column; align-items: center; gap: 10px;
  }
  .back-brand .brand-mark { margin: 0; width: 56px; height: 56px; }
  .back-brand .brand-name { font-size: 12.5px; text-align: center; }
  .person-name {
    position: absolute; right: 16px; top: 32px;
    font-size: 21px; font-weight: 600; letter-spacing: 1px;
  }
  .person-name__last { color: var(--red); }
  .contacts { position: absolute; left: 196px; right: 0; top: 85px; list-style: none; }
  .contacts li {
    display: flex; align-items: center; gap: 10px;
    height: 35px; font-size: 10.5px; font-weight: 500;
    border-top: 1.5px solid var(--ink);
  }
  .contacts li:nth-child(odd) { border-top-color: var(--ink); }
  .contacts li:nth-child(even) { border-top-color: var(--red); }
  .contacts li:last-child { border-bottom: 1.5px solid var(--red); }
  .contacts li:nth-child(2) { border-top-color: var(--red); }
  .contacts li:nth-child(3) { border-top-color: var(--ink); }
  .contact-icon { width: 15px; height: 15px; flex: none; }
</style>
</head>
<body>
  <section class="card card--front" aria-label="Business card front">
    <div class="front-panel">
      <div class="brand-mark" aria-hidden="true"></div>
      <p class="front-panel__services">First Aid Training<br>WHS Training</p>
    </div>
    <div class="front-body">
      <h1 class="brand-name">Brindlewood<br>First Aid</h1>
      <p class="tagline">ONSITE TRAINING - WE CAN COME TO YOU</p>
      <ul class="benefits">
        <li><span class="bullet"></span>TIME EFFICIENT</li>
        <li><span class="bullet"></span>COST EFFECTIVE</li>
        <li><span class="bullet"></span>MINIMISE DOWNTIME FOR YOUR TEAM</li>
      </ul>
    </div>
  </section>

  <section class="card card--back" aria-label="Business card back">
    <div class="back-strip"></div>
    <div class="back-tab back-tab--top"></div>
    <div class="back-tab back-tab--bottom"></div>
    <div class="back-brand">
      <div class="brand-mark" aria-hidden="true"></div>
      <p class="brand-name">Brindlewood<br>First Aid</p>
    </div>
    <h2 class="person-name">DANIEL <span class="person-name__last">HARTLEY</span></h2>
    <ul class="contacts">
      <li>
        <svg class="contact-icon" viewBox="0 0 16 16" aria-hidden="true">
          <rect x="2" y="2" width="14" height="14" fill="#111"/>
          <rect x="0" y="0" width="14" height="14" fill="#ee0000"/>
          <path d="M4 3.5l2 0 .8 2.2-1.2.9a6 6 0 0 0 2.8 2.8l.9-1.2 2.2.8 0 2a1 1 0 0 1-1 1A7.5 7.5 0 0 1 3 4.5a1 1 0 0 1 1-1z" fill="#fff"/>
        </svg>
        0400 512 386
      </li>
      <li>
        <svg class="contact-icon" viewBox="0 0 16 16" aria-hidden="true">
          <rect x="2" y="2" width="14" height="14" fill="#ee0000"/>
          <rect x="0" y="0" width="14" height="14" fill="#fff" stroke="#111" stroke-width="1.5"/>
          <rect x="3" y="4" width="8" height="6" fill="none" stroke="#111" stroke-width="1.3"/>
          <path d="M3 4l4 3.5L11 4" fill="none" stroke="#111" stroke-width="1.3"/>
        </svg>
        help@brindlewoodfa.com.au
      </li>
      <li>
        <svg class="contact-icon" viewBox="0 0 16 16" aria-hidden="true">
          <rect x="2" y="2" width="14" height="14" fill="#111"/>
          <rect x="0" y="0" width="14" height="14" fill="#ee0000"/>
          <circle cx="7" cy="7" r="4" fill="none" stroke="#fff" stroke-width="1.1"/>
          <path d="M3 7h8M7 3v8" stroke="#fff" stroke-width="1"/>
        </svg>
        brindlewoodfa.com.au
      </li>
    </ul>
  </section>
</body>
</html>
```